First Birthday Party Invitation

We need a flyer/invitation design for our baby girl Marisol's first birthday party. We want the design to look like a club event flyer. The party will have a sailing/nautical theme and will be at a marina but in Miami so the invite must have a cool, non-baby, non-kitchy vibe.

Here's the text...feel free to play around with it!

Welcome Aboard! 

We'll have lots of fun

Our little Marisol is turning one!

You're invited to a party

on Saturday, August 7th from 5 - 7 p.m.

Tide-And-Rope Miami

Third Floor
4187 North Coralwind Avenue
Miami, FL 33149-7812
Parking tickets will be validated 

Please RSVP by July 31st to MarisolBirthday@bluefinmail.test or 305.482.9067

Arrive early at 4 p.m. to join us on a short pre-party boat tour of the Miami skyline

Flyer should be one-sided only.  It will be printed in color and also emailed. 

Important update - please add small text that says "No gifts please.  A contribution to Tide And Rope's programs would be greatly appreciated."

```html
<!DOCTYPE html>
<html lang="en">
<head>
<meta charset="utf-8">
<title>Marisol's 1st Birthday – Welcome Aboard</title>
<link href="https://fonts.googleapis.com/css2?family=Abril+Fatface&display=swap" rel="stylesheet">
<style>
  :root {
    --sea-teal: #8ab3ad;
    --paper: #dcdfd1;
    --rope: #e8b457;
    --wood: #8e6549;
    --olive: #b6ba7c;
    --ribbon-text: #e6e6d8;
  }
  html, body {
    margin: 0;
    padding: 0;
    overflow: hidden;
    background: var(--paper);
  }
  .invitation {
    display: block;
    width: 959px;
    height: 1200px;
  }
  .headline {
    font-family: "Abril Fatface", "Playfair Display", serif;
    fill: var(--sea-teal);
  }
  .detail {
    font-family: "Abril Fatface", "Playfair Display", serif;
    fill: var(--sea-teal);
  }
  .detail-accent { fill: var(--wood); }
  .ribbon-text {
    font-family: "Abril Fatface", serif;
    fill: var(--ribbon-text);
  }
  .small-word { font-size: 0.7em; }
</style>
</head>
<body>
<svg class="invitation" viewBox="0 0 959 1200" xmlns="http://www.w3.org/2000/svg">
  <defs>
    <linearGradient id="emblem-tone" x1="0" y1="0" x2="0" y2="1">
      <stop offset="0" stop-color="#c9ccaa"/>
      <stop offset="0.55" stop-color="var(--olive)"/>
      <stop offset="1" stop-color="var(--wood)"/>
    </linearGradient>
    <path id="preparty-arc" d="M352,134 Q480,40 608,134"/>
  </defs>

  <!-- frame -->
  <rect class="frame-band" x="0" y="0" width="959" height="1200" fill="var(--sea-teal)"/>
  <rect class="frame-paper" x="24" y="24" width="911" height="1152" rx="24" fill="var(--paper)" stroke="var(--rope)" stroke-width="5"/>

  <!-- pre-party info -->
  <g class="headline arrive-note">
    <text x="60" y="116" font-size="80" textLength="200" lengthAdjust="spacingAndGlyphs">ARRIVE</text>
    <text x="60" y="176" font-size="72" textLength="218" lengthAdjust="spacingAndGlyphs">BY 4 P.M.</text>
    <text x="60" y="268" font-size="106" textLength="208" lengthAdjust="spacingAndGlyphs">FOR A</text>
  </g>
  <text class="headline preparty" font-size="50">
    <textPath href="#preparty-arc" startOffset="50%" text-anchor="middle">PRE-PARTY</textPath>
  </text>
  <g class="headline tour-note">
    <text x="694" y="140" font-size="112" textLength="208" lengthAdjust="spacingAndGlyphs">TOUR</text>
    <text x="694" y="200" font-size="68" textLength="210" lengthAdjust="spacingAndGlyphs">OF MIAMI</text>
    <text x="694" y="268" font-size="80" textLength="210" lengthAdjust="spacingAndGlyphs">SKYLINE</text>
  </g>

  <!-- party date and time -->
  <g class="detail when">
    <text x="56" y="350" font-size="26" textLength="190" lengthAdjust="spacingAndGlyphs">YOU’RE INVITED</text>
    <text x="56" y="382" font-size="26" textLength="150" lengthAdjust="spacingAndGlyphs">TO A PARTY ON</text>
    <rect x="56" y="398" width="190" height="4" rx="2" fill="var(--sea-teal)"/>
    <text x="56" y="448" font-size="44" textLength="190" lengthAdjust="spacingAndGlyphs">SATURDAY</text>
    <text class="detail-accent" x="56" y="500" font-size="46" textLength="190" lengthAdjust="spacingAndGlyphs">AUGUST 7th</text>
    <text x="56" y="560" font-size="54" textLength="190" lengthAdjust="spacingAndGlyphs">5 – 7 P.M.</text>
  </g>

  <!-- venue -->
  <g class="detail where">
    <text x="716" y="350" font-size="28" textLength="196" lengthAdjust="spacingAndGlyphs">TIDE-AND-ROPE</text>
    <text x="716" y="386" font-size="34" textLength="120" lengthAdjust="spacingAndGlyphs">MIAMI</text>
    <rect x="716" y="402" width="196" height="4" rx="2" fill="var(--sea-teal)"/>
    <text class="detail-accent" x="716" y="440" font-size="26" textLength="150" lengthAdjust="spacingAndGlyphs">THIRD FLOOR</text>
    <text x="716" y="472" font-size="22" textLength="196" lengthAdjust="spacingAndGlyphs">4187 NORTH CORALWIND</text>
    <text x="716" y="500" font-size="22" textLength="100" lengthAdjust="spacingAndGlyphs">AVENUE</text>
    <text x="716" y="528" font-size="22" textLength="196" lengthAdjust="spacingAndGlyphs">MIAMI, FL 33149-7812</text>
    <text x="716" y="566" font-size="18" textLength="196" lengthAdjust="spacingAndGlyphs">PARKING TICKETS WILL</text>
    <text x="716" y="590" font-size="18" textLength="130" lengthAdjust="spacingAndGlyphs">BE VALIDATED</text>
  </g>

  <!-- nautical emblem -->
  <path class="emblem-art" role="img" aria-label="Ship's wheel framing a sailboat against a sunburst, with tropical flowers"
        d="M288,664 L288,330 Q288,236 476,236 Q664,236 664,330 L664,664 Z" fill="url(#emblem-tone)"/>
  <polygon class="birthday-ribbon" points="258,500 704,448 694,588 264,634" fill="var(--sea-teal)" stroke="var(--paper)" stroke-width="4"/>
  <text class="ribbon-text" x="480" y="572" font-size="60" text-anchor="middle" textLength="390" lengthAdjust="spacingAndGlyphs" transform="rotate(-6 480 552)">Happy 1st Birthday</text>
  <rect class="name-plate" x="342" y="664" width="278" height="84" rx="18" fill="var(--sea-teal)" stroke="var(--paper)" stroke-width="5"/>
  <text class="ribbon-text name" x="481" y="728" font-size="62" text-anchor="middle" textLength="244" lengthAdjust="spacingAndGlyphs">Marisol</text>
  <rect class="palm-art" role="img" aria-label="Small palm tree on an island" x="680" y="684" width="54" height="100" rx="10" fill="var(--sea-teal)"/>

  <!-- welcome block -->
  <text class="headline welcome" x="0" y="0" font-size="42" textLength="128" lengthAdjust="spacingAndGlyphs" transform="translate(244 920) rotate(-90)">WELCOME</text>
  <text class="headline aboard" x="264" y="920" font-size="186" textLength="488" lengthAdjust="spacingAndGlyphs">ABOARD</text>
  <text class="headline fun-line" x="204" y="1000" font-size="94" textLength="544" lengthAdjust="spacingAndGlyphs">WE’LL HAVE LOTS OF FUN</text>
  <text class="headline turning-one" x="208" y="1046" font-size="48" textLength="540" lengthAdjust="spacingAndGlyphs">OUR <tspan class="small-word">LITTLE</tspan> MARISOL IS TURNING ONE!</text>
  <rect class="divider" x="188" y="1058" width="580" height="8" rx="4" fill="var(--sea-teal)"/>
  <text class="headline rsvp" x="196" y="1098" font-size="24" textLength="562" lengthAdjust="spacingAndGlyphs">PLEASE RSVP BY JULY 31st TO MarisolBirthday@bluefinmail.test or 305.482.9067</text>
  <text class="detail gifts" x="477" y="1130" font-size="17" text-anchor="middle" textLength="380" lengthAdjust="spacingAndGlyphs">NO GIFTS PLEASE. A CONTRIBUTION TO TIDE AND ROPE’S</text>
  <text class="detail gifts" x="477" y="1152" font-size="17" text-anchor="middle" textLength="300" lengthAdjust="spacingAndGlyphs">PROGRAMS WOULD BE GREATLY APPRECIATED.</text>
</svg>
</body>
</html>
```